Letterhead for a German Distribution/Manufacturing Company

We need a professional Letterhead in a unique Design.
not to playful.
The Letterhead has to show show that we are a international company with headquater in Germany.
all details like adress, Vat Tax Number, Bank Accout, Eori, email, Company number has to be on the Letterhead.
for example use: VAT TAX DE5140683 Bank Account: Halmer Kreditbank IBAN DE417052381ß240316 Swift: HKRB0513742 EORI 3150827469 Company Number: HRB 58106 Adress: VOLINTRA UG Tannwiesen Strasse 7 Postal Code 09385 City Burgstädt Country: Germany Email: info@volintra-mail.net
the design can be colored but doesnt have to be
Industry/Entity Type
Manufacturing and international distribution
Requirements
Must have
- show that we are a international company with headquater in Germany. our company infos and logo

```html
<!DOCTYPE html>
<html lang="en">
<head>
<meta charset="utf-8">
<title>VOLINTRA Letterhead</title>
<link rel="stylesheet" href="https://fonts.googleapis.com/css2?family=Jost:wght@400&display=swap">
<style>
  :root {
    --backdrop: #f2f2f2;
    --paper: #ffffff;
    --frame: #555555;
    --steel-grey: #98999d;
    --signal-orange: #e87e04;
    --brand-orange: #e8640c;
    --ink: #1e1e1e;
  }
  * { margin: 0; padding: 0; box-sizing: border-box; }
  html, body {
    width: 800px; height: 1200px; overflow: hidden;
    background: var(--backdrop);
  }
  .canvas { position: relative; width: 800px; height: 1200px; }
  .letterhead {
    position: absolute; left: 20px; top: 108px;
    width: 760px; height: 984px;
    background: var(--paper);
    border: 1px solid var(--frame);
    overflow: hidden;
    font-family: "Jost", sans-serif;
  }
  .accent-shapes { position: absolute; inset: 0; }
  .accent-grey { fill: var(--steel-grey); }
  .accent-orange { fill: var(--signal-orange); }
  .brand {
    position: absolute; left: 86px; top: 104px;
    display: flex; align-items: center; gap: 10px;
  }
  .brand-dot {
    width: 30px; height: 30px; border-radius: 50%;
    background: var(--brand-orange);
  }
  .brand-name {
    font-size: 40px; font-weight: 400; letter-spacing: 1px;
    color: var(--brand-orange); line-height: 1;
  }
  .company-details {
    position: absolute; left: 436px; top: 876px;
    width: 284px;
    font-size: 9.3px; line-height: 12.6px;
    letter-spacing: -0.1px;
    color: var(--ink); white-space: nowrap;
  }
  .company-details .label { color: var(--signal-orange); }
</style>
</head>
<body>
<div class="canvas">
  <div class="letterhead">
    <svg class="accent-shapes" width="760" height="984" viewBox="0 0 760 984" aria-hidden="true">
      <polygon class="accent-grey" points="0,0 141,0 125.4,56 54.8,56 54.8,203.4 84.9,203.4 0,512.5"/>
      <polygon class="accent-orange" points="760,669 760,984 674,984 683.8,949.3 727.6,949.3 727.6,858 708.7,858"/>
    </svg>

    <div class="brand">
      <span class="brand-dot"></span>
      <span class="brand-name">VOLINTRA</span>
    </div>

    <div class="company-details">
      <div><span class="label">VAT TAX</span> DE5140683 - <span class="label">Company Number</span> HRB 58106</div>
      <div><span class="label">Bank Account</span> Halmer Kreditbank IBAN DE417052381ß240316</div>
      <div><span class="label">Swift</span> HKRB0513742 EORI 3150827469</div>
      <div><span class="label">Address</span> VOLINTRA UG Tannwiesen Strasse 7 Postal Code 09385 City</div>
      <div><span class="label">Burgstädt Country Germany Email</span> info@volintra-mail.net</div>
    </div>
  </div>
</div>
</body>
</html>
```